Business Card design

Keen on a very modern design with using the red star as a feature point preferably will have it printed with red foiling.

Target Market(s)

Cosmetics

Industry/Entity Type

Cosmetics

Contact Information for Business Card

Marnie Telford
Director
17 Brisbrook Lane
Wyndale Heights Victoria
Australia 3033
marnie@glowcratesupply.com.au

Font styles to use
Sans Serif

Colors
ec1f27
000000

Requirements
Must have
• Keen on some red stars on back with black background and I may get the red components printed as red foiling potentially

```html
<!DOCTYPE html>
<html lang="en">
<head>
<meta charset="utf-8">
<title>Glowcrate Business Card</title>
<link rel="stylesheet" href="https://fonts.googleapis.com/css2?family=Lato:wght@400;700;900&display=swap">
<style>
  :root {
    --brand-red: #ec1f27;
    --ink: #000000;
    --text: #1d1d1f;
    --paper: #ffffff;
    --stage: #1b1b1d;
  }
  * { margin: 0; padding: 0; box-sizing: border-box; }
  html, body {
    width: 1200px;
    height: 1200px;
    overflow: hidden;
    background: var(--stage);
    font-family: "Lato", Arial, sans-serif;
  }
  .sheet {
    position: relative;
    width: 1200px;
    height: 1200px;
  }
  .card {
    position: absolute;
    left: 150px;
    width: 900px;
    height: 514px;
  }
  .card--back {
    top: 70px;
    background: var(--ink);
    display: flex;
    align-items: center;
    justify-content: center;
  }
  .card--back .brand-name {
    font-weight: 900;
    font-size: 64px;
    letter-spacing: -1px;
    color: var(--brand-red);
  }
  .card--front {
    top: 616px;
    background: var(--paper);
    color: var(--text);
  }
  .front-brand {
    position: absolute;
    left: 58px;
    top: 70px;
    display: flex;
    align-items: center;
    gap: 18px;
  }
  .front-brand .brand-mark {
    width: 30px;
    height: 30px;
    border-radius: 50%;
    background: var(--brand-red);
  }
  .front-brand .brand-name {
    font-weight: 900;
    font-size: 92px;
    letter-spacing: -3px;
    line-height: 1;
    color: var(--text);
  }
  .contact-block {
    position: absolute;
    right: 58px;
    bottom: 70px;
    display: flex;
    align-items: stretch;
    gap: 26px;
  }
  .contact-list {
    list-style: none;
    text-align: right;
    font-size: 22px;
    line-height: 34px;
  }
  .contact-list li {
    display: flex;
    align-items: center;
    justify-content: flex-end;
    gap: 12px;
  }
  .contact-list svg {
    width: 20px;
    height: 20px;
    flex: none;
    fill: var(--brand-red);
  }
  .divider {
    width: 2px;
    background: var(--text);
  }
  .person {
    display: flex;
    flex-direction: column;
    justify-content: center;
  }
  .person-name {
    font-weight: 900;
    font-size: 30px;
    line-height: 36px;
  }
  .person-role {
    font-size: 25px;
    line-height: 30px;
    color: var(--brand-red);
  }
</style>
</head>
<body>
<main class="sheet">
  <section class="card card--back" aria-label="Card back">
    <span class="brand-name">Glowcrate</span>
  </section>

  <section class="card card--front" aria-label="Card front">
    <div class="front-brand">
      <span class="brand-mark"></span>
      <span class="brand-name">Glowcrate</span>
    </div>

    <div class="contact-block">
      <ul class="contact-list">
        <li>098-517-2260
          <svg viewBox="0 0 24 24" aria-hidden="true"><path d="M6.6 10.8a15.1 15.1 0 0 0 6.6 6.6l2.2-2.2a1 1 0 0 1 1-.25 11.4 11.4 0 0 0 3.6.57 1 1 0 0 1 1 1V20a1 1 0 0 1-1 1A17 17 0 0 1 3 4a1 1 0 0 1 1-1h3.5a1 1 0 0 1 1 1c0 1.25.2 2.45.57 3.57a1 1 0 0 1-.25 1z"/></svg>
        </li>
        <li>marnie@glowcratesupply.com.au
          <svg viewBox="0 0 24 24" aria-hidden="true"><path d="M2 5h20v14H2zm2 2v.4l8 5.2 8-5.2V7zm0 2.8V17h16V9.8l-8 5.2z"/></svg>
        </li>
        <li>17 Brisbrook Lane, Wyndale Heights Victoria, Australia 3033
          <svg viewBox="0 0 24 24" aria-hidden="true"><path d="M12 2a7 7 0 0 0-7 7c0 5.2 7 13 7 13s7-7.8 7-13a7 7 0 0 0-7-7zm0 9.5A2.5 2.5 0 1 1 12 6.5a2.5 2.5 0 0 1 0 5z"/></svg>
        </li>
      </ul>
      <span class="divider"></span>
      <div class="person">
        <span class="person-name">Marnie Telford</span>
        <span class="person-role">Director</span>
      </div>
    </div>
  </section>
</main>
</body>
</html>
```